Become an EMT and Serve your community!

We are looking to design a postcard that will be mailed to surrounding communities that notifies them of our upcoming EMT class with an emphasis of serving their community. We are looking for a design that grabs peoples attention and motivates them to sign up and serve their community. Our primary colors are red and blue. We would like to incorporate the Institute logo as well as one or two photos. We do have more photos available upon request. Our Institute website is www.halvorsenacademy.net for more material. It is important that the postcard meets mailing guidelines.

Target Market(s)

Local community members

Industry/Entity Type

Education

Font styles to use
Sans Serif

Colors
f04a50
3176b5
0255a3
eaf1f7

Requirements
Must have
• Dates
Prices
Contact info
Look interesting
Convey the message of “Serving your Community”
Nice to have
• Clear information
Concise
Incorporate an action shot
Should not have
• Generic EMS logos

```html
<!DOCTYPE html>
<html lang="en">
<head>
<meta charset="utf-8">
<title>2020 Summer EMT Class – Halvorsen Academy of EMS</title>
<link rel="stylesheet" href="https://fonts.googleapis.com/css2?family=Montserrat:wght@600;700;800;900&family=Yellowtail&display=swap">
<style>
  :root {
    --navy: #2e2b6e;
    --red: #f04a50;
    --ice: #eaf1f7;
    --ink: #3a3a3c;
    --white: #ffffff;
    --backdrop: #d1d2d4;
  }
  * { box-sizing: border-box; margin: 0; padding: 0; }
  html, body {
    width: 1200px; height: 1013px; overflow: hidden;
    background: var(--backdrop);
    font-family: "Montserrat", Arial, sans-serif;
  }
  .postcard {
    position: absolute; left: 186px; top: 230px;
    width: 829px; height: 553px;
    background: var(--white); overflow: hidden;
  }
  .top-rule { position: absolute; left: 0; top: 0; width: 100%; height: 18px; background: var(--navy); }
  .class-title {
    position: absolute; left: 77px; top: 22px;
    font-family: "Yellowtail", cursive; font-size: 38px; color: var(--navy);
    line-height: 1; white-space: nowrap;
  }
  .headline-band { position: absolute; left: 0; top: 76px; width: 100%; height: 172px; background: var(--navy); }
  .headline {
    position: absolute; left: 75px; top: 90px;
    font-weight: 900; font-size: 46px; line-height: 46px; color: var(--white);
    letter-spacing: -0.3px;
  }
  .photo-area { position: absolute; left: 0; top: 0; width: 829px; height: 553px; }
  .register-band { position: absolute; left: 0; top: 456px; width: 100%; height: 97px; background: var(--red); }
  .benefits-label {
    position: absolute; left: 30px; top: 286px;
    font-weight: 900; font-size: 16px; color: var(--navy); letter-spacing: 0.2px;
  }
  .benefit { position: absolute; display: flex; align-items: center; gap: 11px; }
  .benefit .tick { width: 37px; height: 37px; flex: none; }
  .benefit p { font-weight: 700; font-size: 19px; line-height: 19px; color: var(--ink); }
  .benefit--equipment { left: 28px; top: 322px; }
  .benefit--instructors { left: 286px; top: 322px; }
  .benefit--ambulance { left: 28px; top: 385px; }
  .register-call {
    position: absolute; left: 49px; top: 477px;
    font-weight: 900; font-size: 27px; line-height: 26px; color: var(--white);
  }
  .divider { position: absolute; left: 206px; top: 481px; width: 3px; height: 48px; background: #f78a8e; }
  .contact { position: absolute; left: 219px; display: flex; align-items: center; gap: 6px;
    font-weight: 700; font-size: 18px; color: var(--white); }
  .contact svg { width: 19px; height: 19px; }
  .contact--phone { top: 476px; }
  .contact--web { top: 501px; }
  .academy-seal {
    position: absolute; left: 524px; top: 42px; width: 238px; height: 238px;
    border-radius: 50%; background: var(--navy); border: 9px solid var(--white);
    box-shadow: 0 0 0 2px var(--navy);
    display: flex; align-items: center; justify-content: center; text-align: center;
  }
  .academy-seal span { font-weight: 800; font-size: 22px; line-height: 27px; color: var(--white); }
</style>
</head>
<body>
  <div class="postcard">
    <div class="top-rule"></div>
    <div class="class-title">2020 Summer EMT Class</div>
    <div class="headline-band"></div>
    <h1 class="headline">Become an EMT<br>and Serve your<br>community!</h1>

    <div class="register-band"></div>

    <svg class="photo-area" viewBox="0 0 829 553" role="img" aria-label="Photo of two EMTs in red jackets treating a patient inside an ambulance">
      <defs>
        <linearGradient id="ambulance-scene" x1="0" y1="0" x2="1" y2="1">
          <stop offset="0" stop-color="#6f6e72"/>
          <stop offset="0.45" stop-color="#b9b6b6"/>
          <stop offset="0.75" stop-color="#c22a2e"/>
          <stop offset="1" stop-color="#8c2a22"/>
        </linearGradient>
      </defs>
      <path d="M488 248 C468 330 515 480 617 553 L829 553 L829 248 Z" fill="url(#ambulance-scene)"/>
      <path d="M488 248 C468 330 515 480 617 553" fill="none" stroke="var(--ice)" stroke-width="9"/>
    </svg>

    <div class="academy-seal"><span>Halvorsen<br>Academy<br>of EMS</span></div>

    <h2 class="benefits-label">AS A STUDENT YOU WILL HAVE ACCESS TO;</h2>

    <div class="benefit benefit--equipment">
      <svg class="tick" viewBox="0 0 36 36"><circle cx="18" cy="18" r="18" fill="var(--red)"/><path d="M10.5 18.5l5 5 10-10" fill="none" stroke="#fff" stroke-width="3.2" stroke-linecap="round" stroke-linejoin="round"/></svg>
      <p>Cutting-edge<br>training equipment</p>
    </div>
    <div class="benefit benefit--instructors">
      <svg class="tick" viewBox="0 0 36 36"><circle cx="18" cy="18" r="18" fill="var(--red)"/><path d="M10.5 18.5l5 5 10-10" fill="none" stroke="#fff" stroke-width="3.2" stroke-linecap="round" stroke-linejoin="round"/></svg>
      <p>Experienced<br>Instructors</p>
    </div>
    <div class="benefit benefit--ambulance">
      <svg class="tick" viewBox="0 0 36 36"><circle cx="18" cy="18" r="18" fill="var(--red)"/><path d="M10.5 18.5l5 5 10-10" fill="none" stroke="#fff" stroke-width="3.2" stroke-linecap="round" stroke-linejoin="round"/></svg>
      <p>Train on a 911 Ambulance<br>through Halvorsen EMS</p>
    </div>

    <div class="register-call">REGISTER<br>TODAY</div>
    <div class="divider"></div>
    <div class="contact contact--phone">
      <svg viewBox="0 0 24 24" fill="none" stroke="#fff" stroke-width="2" stroke-linecap="round" stroke-linejoin="round"><path d="M22 16.9v3a2 2 0 0 1-2.2 2 19.8 19.8 0 0 1-8.6-3.1 19.5 19.5 0 0 1-6-6A19.8 19.8 0 0 1 2.1 4.2 2 2 0 0 1 4.1 2h3a2 2 0 0 1 2 1.7c.1.9.4 1.8.7 2.7a2 2 0 0 1-.5 2.1L8 9.8a16 16 0 0 0 6 6l1.3-1.3a2 2 0 0 1 2.1-.4c.9.3 1.8.6 2.7.7a2 2 0 0 1 1.7 2z"/><path d="M15 2a7 7 0 0 1 7 7M15 6a3 3 0 0 1 3 3"/></svg>
      <span>603-555-0148</span>
    </div>
    <div class="contact contact--web">
      <svg viewBox="0 0 24 24" fill="none" stroke="#fff" stroke-width="2"><circle cx="12" cy="12" r="10"/><path d="M2 12h20M12 2a15 15 0 0 1 0 20M12 2a15 15 0 0 0 0 20"/></svg>
      <span>www.halvorsenacademy.net</span>
    </div>
  </div>
</body>
</html>
```